Lumora Studio
Business Card, Letterhead, Envelope, Fax
Professional
Marcus Pellway
President / CEO, Lumora Studio
41B W Alder Road, Suite 6
PO Box 7382
Watkinsville, Georgia 30912
marcus@lumoraweb.example
www.lumoraweb.example
We would also like stationary (letterhead, business card, fax, and envelope - window and windowless).
Please also include QTA Accreditation logo that was uploaded.
Please provide these with an editable format, preferrably Microsoft Word - so that we can create more for additional staff.
Logo and web address (www.lumoraweb.example)
Services can be included (optional)
Web Design and Development
Internet Marketing
E-mail Marketing
Content Management Systems
Graphic and Print Design
Application Development
Consulting
Search Engine Optimization
E-Commerce
QTA Accreditation logo to be included
eps(vector) on white background
ai(vector) on white background
eps (vector) vertical on white background
ai(vector) vertical on white background

```html
<!DOCTYPE html>
<html lang="en">
<head>
<meta charset="utf-8">
<title>Lumora Studio – Business Card</title>
<link rel="stylesheet" href="https://fonts.googleapis.com/css2?family=Arimo:wght@400;700&display=swap">
<style>
  :root {
    --backdrop: #d9dadb;
    --card-white: #ffffff;
    --navy: #1d3a63;
    --navy-deep: #142c4f;
    --navy-light: #2b5283;
    --ink: #2a2f36;
    --muted: #6b7178;
    --pale-blue: #a9bfdc;
  }
  * { margin: 0; padding: 0; box-sizing: border-box; }
  html, body {
    width: 1200px; height: 871px; overflow: hidden;
    background: var(--backdrop);
    font-family: "Arimo", Arial, sans-serif;
  }
  .canvas { position: relative; width: 1200px; height: 871px; }

  .card {
    position: absolute;
    width: 420px; height: 257px;
    border-radius: 16px;
    box-shadow: 0 6px 18px rgba(0,0,0,0.25);
    overflow: hidden;
  }

  /* Front */
  .card-front { left: 233px; top: 175px; background: var(--card-white); }
  .holder { position: absolute; left: 26px; top: 22px; }
  .holder-name { font-size: 17px; font-weight: 700; color: var(--navy); }
  .holder-title { font-size: 9px; color: var(--muted); margin-top: 2px; }

  .front-brand { position: absolute; left: 22px; top: 126px; text-align: center; width: 190px; }
  .brand-row { display: flex; align-items: center; justify-content: center; gap: 8px; }
  .brand-dot { width: 24px; height: 24px; border-radius: 50%; background: var(--navy); flex: none; }
  .brand-name { font-size: 20px; font-weight: 700; color: var(--navy); letter-spacing: -0.3px; white-space: nowrap; }
  .tagline {
    display: inline-block; margin-top: 4px;
    font-size: 7px; color: var(--ink); letter-spacing: 0.2px;
  }

  .contact {
    position: absolute; left: 240px; top: 104px;
    font-size: 7.5px; line-height: 10.5px; color: var(--muted);
    list-style: none;
  }

  /* Back */
  .card-back {
    left: 504px; top: 451px;
    background: radial-gradient(ellipse at 40% 35%, var(--navy-light) 0%, var(--navy) 55%, var(--navy-deep) 100%);
  }
  .back-brand { position: absolute; left: 0; right: 0; top: 82px; text-align: center; }
  .back-brand .brand-dot { width: 32px; height: 32px; background: #e9eef5; }
  .back-brand .brand-name { font-size: 28px; color: #ffffff; }
  .back-brand .tagline {
    margin-top: 6px; padding: 3px 8px;
    font-size: 8.5px; color: #ffffff;
    background: rgba(255,255,255,0.12);
    border: 1px solid rgba(255,255,255,0.35);
  }
  .web {
    position: absolute; left: 0; right: 0; bottom: 22px; text-align: center;
    font-size: 10px; letter-spacing: 3px; color: var(--pale-blue);
  }
</style>
</head>
<body>
<main class="canvas">
  <section class="card card-front" aria-label="Business card front">
    <div class="holder">
      <p class="holder-name">Marcus Pellway</p>
      <p class="holder-title">President / CEO, Lumora Studio</p>
    </div>
    <div class="front-brand">
      <div class="brand-row">
        <span class="brand-dot"></span>
        <span class="brand-name">Lumora Studio</span>
      </div>
      <span class="tagline">Insight | Craft | Momentum</span>
    </div>
    <ul class="contact">
      <li>41B W Alder Road, Suite 6</li>
      <li>PO Box 7382</li>
      <li>Harlow Bend, Ohio 30912</li>
      <li>Toll Free: (877) 555-0142</li>
      <li>P: (418) 555-0187</li>
      <li>F: (418) 555-0163</li>
      <li>C: (418) 555-0129</li>
      <li>E: marcus@lumoraweb.example</li>
      <li>www.lumoraweb.example</li>
    </ul>
  </section>

  <section class="card card-back" aria-label="Business card back">
    <div class="back-brand">
      <div class="brand-row">
        <span class="brand-dot"></span>
        <span class="brand-name">Lumora Studio</span>
      </div>
      <span class="tagline">Insight | Craft | Momentum</span>
    </div>
    <p class="web">www.lumoraweb.example</p>
  </section>
</main>
</body>
</html>
```